Electrician Business Card/ company logo/small business

New Business Cards and logo needed that will catch peoples eye and say we went that extra step. Attached is a design possibly to be incorporated, if u have your own great, lets see it!... This will be a small local business. thank you for all you do!
Corvane Electric
Wren Osloby Owner
Journeyman Electrician
phone 1.360.428.6037
email: KLXCorvaneElectric@mailvex.net
call for free estimate!

Target Market(s)

support small local business

Industry/Entity Type

Electrical,

Contact Information for Business Card

name, title,company/ logo, phone, email, free estimate

Font styles to use
Other font styles liked:
• easy to read

Colors

Designer to choose colors to be used in the design.

Requirements
Must have
• eye catching everything! logo and corvane electric listed on business card/logo, incorp logo in the background of card
Nice to have
• lightening bolts in eyes or around the triangle? vertical, modern, any design that would be unique and stand out
Should not have
• pinks, reds, yellows,brown

```html
<!DOCTYPE html>
<html lang="en">
<head>
<meta charset="utf-8">
<title>Corvane Electric – Business Card</title>
<link href="https://fonts.googleapis.com/css2?family=Poppins:wght@400;500;600;700&display=swap" rel="stylesheet">
<style>
  :root{
    --page:#d9d6d0;
    --card:#1a1847;
    --card-deep:#14123a;
    --mark:#7d86f2;
    --mark-dot:#3a3f9a;
    --white:#ffffff;
    --accent:#5ad0e6;
    --icon:#5ad0e6;
    --rule:#c9c9d8;
  }
  *{margin:0;padding:0;box-sizing:border-box}
  html,body{width:900px;height:1200px;overflow:hidden}
  body{background:var(--page);position:relative;font-family:"Poppins",sans-serif}
  .card{
    position:absolute;left:82px;width:733px;height:427px;border-radius:22px;overflow:hidden;
    background:linear-gradient(120deg,var(--card-deep) 0%,var(--card) 55%,#1f2160 100%);
  }
  .card--front{top:138px}
  .card--back{top:633px}
  .storm{position:absolute;inset:0}
  .card--front .storm{background:radial-gradient(ellipse 45% 60% at 78% 35%,rgba(70,80,170,.45),transparent 70%)}
  .card--back .storm{background:
    radial-gradient(ellipse 35% 55% at 15% 55%,rgba(60,70,150,.35),transparent 70%),
    radial-gradient(ellipse 35% 55% at 85% 40%,rgba(60,70,150,.35),transparent 70%)}
  .brand{position:absolute;display:flex;flex-direction:column;align-items:center;transform:translateX(-50%)}
  .brand__dot{width:96px;height:96px;border-radius:50%;background:var(--mark-dot);margin-bottom:62px}
  .brand__name{color:var(--mark);font-weight:600;font-size:34px;letter-spacing:6px;line-height:37px;text-align:center;text-transform:uppercase;white-space:nowrap}
  .card--front .brand{left:180px;top:70px}
  .card--back .brand{left:368px;top:65px}
  .divider{position:absolute;left:326px;top:70px;width:1px;height:274px;background:var(--rule);opacity:.8}
  .contact{position:absolute;left:361px;top:146px;color:var(--white)}
  .contact__name{font-weight:600;font-size:17px;letter-spacing:.6px;text-transform:uppercase;line-height:22px}
  .contact__title{font-weight:600;font-size:15px;color:var(--accent);letter-spacing:.5px;text-transform:uppercase;line-height:22px;margin-bottom:14px}
  .contact__row{display:flex;align-items:center;gap:8px;font-size:15px;line-height:27px;white-space:nowrap}
  .contact__row svg{width:19px;height:19px;flex:none}
  .contact__offer{margin-top:12px;font-weight:500;font-size:14px;letter-spacing:.4px;color:var(--accent);line-height:20px}
</style>
</head>
<body>
  <section class="card card--front">
    <div class="storm" role="img" aria-label="Faint lightning bolts across a dark night sky"></div>
    <div class="brand">
      <span class="brand__dot"></span>
      <p class="brand__name">Corvane<br>Electric</p>
    </div>
    <div class="divider"></div>
    <div class="contact">
      <p class="contact__name">Wren Osloby Owner</p>
      <p class="contact__title">Journeyman Electrician</p>
      <p class="contact__row">
        <svg viewBox="0 0 20 20"><circle cx="10" cy="10" r="8.5" fill="none" stroke="var(--icon)" stroke-width="1.3"/><path d="M7 5.5l1.6 2.2-1 1.1c.6 1.3 1.5 2.2 2.7 2.8l1.1-1 2.1 1.5-.8 1.6c-3.3-.3-6.1-3.2-6.4-6.4z" fill="var(--icon)"/></svg>
        1.360.428.6037
      </p>
      <p class="contact__row">
        <svg viewBox="0 0 20 20"><circle cx="10" cy="10" r="8.5" fill="none" stroke="var(--icon)" stroke-width="1.3"/><rect x="5.5" y="7" width="9" height="6.2" rx=".8" fill="none" stroke="var(--icon)" stroke-width="1.2"/><path d="M5.8 7.4L10 10.6l4.2-3.2" fill="none" stroke="var(--icon)" stroke-width="1.2"/></svg>
        KLXCorvaneElectric@mailvex.net
      </p>
      <p class="contact__offer">Call for free estimate!</p>
    </div>
  </section>

  <section class="card card--back">
    <div class="storm" role="img" aria-label="Faint lightning bolts across a dark night sky"></div>
    <div class="brand">
      <span class="brand__dot"></span>
      <p class="brand__name">Corvane<br>Electric</p>
    </div>
  </section>
</body>
</html>
```